Business Card Design Project - KLB

I am looking for a more sophisticated card design for my company,
"The Kestrel Bureau"

We are a consultancy focused on strategy and change in Associations and professional organisations.

I am a lawyer and psychologist with a PhD and so am looking for something that communicates seriousness and credibility but also quirky creative solutions for strategic problems, which is my field of speciality.

I am looking for something that is quietly spoken, rather than loud colours ('credible' and 'creative' are the two adjectives that I think of as competing here).

I particularly like an embossed card style - heavy white card with plain white or white and black or white and grey text.

The key logo image for the company is a question mark and I am open to suggestions and ideas on design.

I have attached a file that includes a couple of styles that have caught my eye and my thoughts on them. Hopefully they communicate what I'm looking for.
Updates

Thank you for all the great suggestions and designs.

I really appreciated the effort and creative energy you put into your designs. I have now closed the project after selecting a design and advising the successful designer of the card that I am happy with.

Regards

Target Market(s)

Organisations (CEO's and Boards), Governments, Legal professionals, Membership Associations and aspiring professionals.

Industry/Entity Type

Lawyer

Requirements
Must have
• The key logo element is a question mark (?) and this needs to be incorporated.

Embossed style - cut outs or other design ideas interest me too.

The attached file has a number of sample ideas and comments on each one that I like.
Should not have
• I like crisp, modern fonts (Myriads etc...) and do not like embellished fonts or Times etc...

```html
<!DOCTYPE html>
<html lang="en">
<head>
<meta charset="utf-8">
<title>The Kestrel Bureau – Business Card</title>
<link rel="stylesheet" href="https://fonts.googleapis.com/css2?family=Source+Sans+3:wght@700&family=PT+Sans+Narrow:wght@400;700&family=Arimo:wght@400&display=swap">
<style>
  :root {
    --card-bg: #2b2a28;
    --card-edge: #4a4946;
    --brand-grey: #8e8e8e;
    --mark-white: #ffffff;
    --text-white: #ffffff;
  }
  * { margin: 0; padding: 0; box-sizing: border-box; }
  html, body {
    width: 1200px;
    height: 752px;
    overflow: hidden;
    background: var(--card-bg);
  }
  .card {
    position: relative;
    width: 1200px;
    height: 752px;
    background: var(--card-bg);
    border: 1px solid var(--card-edge);
    overflow: hidden;
  }
  .brand-mark {
    position: absolute;
    left: 270px;
    top: 34px;
    width: 150px;
    height: 150px;
  }
  .brand-mark circle { fill: var(--mark-white); }
  .brand-name {
    position: absolute;
    left: 52px;
    top: 206px;
    font-family: "Source Sans 3", sans-serif;
    font-weight: 700;
    font-size: 112px;
    line-height: 108px;
    letter-spacing: -1px;
    color: var(--brand-grey);
    white-space: nowrap;
  }
  .brand-name span { display: block; }
  .contact-block {
    position: absolute;
    right: 63px;
    top: 356px;
    text-align: right;
    color: var(--text-white);
  }
  .person-name {
    font-family: "PT Sans Narrow", sans-serif;
    font-weight: 700;
    font-size: 47px;
    line-height: 60px;
  }
  .person-title {
    font-family: "PT Sans Narrow", sans-serif;
    font-weight: 400;
    font-size: 47px;
    line-height: 66px;
    margin-bottom: 4px;
  }
  .contact-line {
    font-family: "Arimo", sans-serif;
    font-size: 33px;
    line-height: 61px;
    letter-spacing: -0.6px;
    white-space: nowrap;
  }
</style>
</head>
<body>
  <div class="card">
    <svg class="brand-mark" viewBox="0 0 150 150" aria-hidden="true">
      <circle cx="75" cy="75" r="75"/>
    </svg>

    <div class="brand-name" aria-label="The Kestrel Bureau">
      <span>The Kestrel</span>
      <span>Bureau</span>
    </div>

    <div class="contact-block">
      <p class="person-name">Dr. Mara Ellison</p>
      <p class="person-title">Director</p>
      <p class="contact-line">M: +61455 203 917</p>
      <p class="contact-line">P: +612 9430 2285</p>
      <p class="contact-line">E: mara@kestrelbureau.com.au</p>
      <p class="contact-line">PO: P.O. Box 4418, Hollins Vale, Sydney, Australia</p>
    </div>
  </div>
</body>
</html>
```